We would like to incorporate our logo into letterhead design and envelopes. We are looking for something that is moderately conservative but not old law firm style. Both the envelopes and the letterhead must have both firm addresses. We would like to incorporate the color of the logo, but only a small amount of color - perhaps on one of the borders. The addresses for the firm locations are listed below. Given that it is a law firm, it needs to somewhat conservative, but not the old school, small black font on cream colored paper design.

The firm addresses are:

27815 N. Harlow Pemberton Pkwy.
Ste 4200
Scottsdale, AZ 85391

6100 W. Cedar Avenue
Ste 700
Burbank, CA 91623

Industry/Entity Type

Legal

Colors

Designer to choose colors to be used in the design.

Requirements
Must have
• Both addresses:
• 27815 N. Harlow Pemberton Pkwy.
• Ste 4200
• Scottsdale, AZ 85391
• 6100 W. Cedar Avenue
• Ste 700
• Burbank, CA 91623
Nice to have
• Small amount of color on border(s) that matches the logo but not too much color

```html
<!DOCTYPE html>
<html lang="en">
<head>
<meta charset="utf-8">
<title>Calder Wynn Law – Letterhead</title>
<link rel="stylesheet" href="https://fonts.googleapis.com/css2?family=Lato:wght@400;700&display=swap">
<style>
  :root {
    --backdrop: #4a4a4a;
    --paper: #ffffff;
    --ink: #1c1c1c;
    --brand: #2b2a8a;
    --brand-light: #6b68c9;
  }
  * { box-sizing: border-box; margin: 0; padding: 0; }
  html, body {
    width: 1200px;
    height: 800px;
    overflow: hidden;
    background: var(--backdrop);
    font-family: "Lato", sans-serif;
  }
  .canvas {
    position: relative;
    width: 1200px;
    height: 800px;
  }
  .letterhead {
    position: absolute;
    left: 330px;
    top: 18px;
    width: 540px;
    height: 764px;
    background: var(--paper);
    overflow: hidden;
    box-shadow: 0 6px 24px rgba(0,0,0,0.35);
  }
  .firm-name {
    position: absolute;
    top: 58px;
    left: 0;
    width: 100%;
    text-align: center;
    font-weight: 400;
    font-size: 38px;
    letter-spacing: 1px;
    text-transform: uppercase;
    color: var(--brand);
  }
  .firm-rule {
    position: absolute;
    top: 108px;
    left: 80px;
    width: 380px;
    height: 1px;
    background: var(--brand);
  }
  .letter-body {
    position: absolute;
    top: 272px;
    left: 88px;
    width: 374px;
    font-size: 10.5px;
    line-height: 1.38;
    color: var(--ink);
    text-align: justify;
  }
  .letter-body p + p { margin-top: 14px; }
  .signature {
    position: absolute;
    top: 526px;
    right: 52px;
    text-align: right;
    font-size: 8.5px;
    line-height: 1.3;
    color: var(--ink);
  }
  .signature .name { text-transform: uppercase; }
  .offices {
    position: absolute;
    top: 570px;
    left: 88px;
    font-size: 9.5px;
    font-style: normal;
    line-height: 1.3;
    color: var(--ink);
  }
  .office-divider {
    width: 82px;
    height: 1px;
    background: var(--brand);
    margin: 5px 0 6px;
  }
  .border-band {
    position: absolute;
    left: 0;
    bottom: 0;
    width: 540px;
    height: 140px;
  }
</style>
</head>
<body>
<div class="canvas">
  <article class="letterhead">
    <h1 class="firm-name">Calder Wynn Law</h1>
    <div class="firm-rule"></div>

    <section class="letter-body">
      <p>Lorem ipsum dolor sit amet, consectetur adipiscing elit, sed do eiusmod tempor incididunt ut labore et dolore magna aliqua. Ut enim ad minim veniam, quis nostrud exercitation ullamco laboris nisi ut aliquip ex ea commodo consequat. Duis aute irure dolor in reprehenderit in voluptate velit esse cillum dolore eu fugiat nulla pariatur. Excepteur sint occaecat cupidatat non proident, sunt in culpa qui officia deserunt mollit anim id est laborum.</p>
      <p>Lorem Ipsum is simply dummy text of the printing and typesetting industry. Lorem Ipsum has been the industry's standard dummy text ever since the 1500s, when an unknown printer took a galley of type and scrambled it to make a type specimen book. It has survived not only five centuries, but also the leap into electronic typesetting, remaining essentially unchanged. It was popularised in the 1960s with the release of Veltrane sheets containing Lorem Ipsum passages, and more recently with desktop publishing software like Corvel PageSet including versions of Lorem Ipsum</p>
    </section>

    <div class="signature">
      <div class="name">Daniel Reyes</div>
      <div class="title">Founder</div>
    </div>

    <address class="offices">
      <div class="office">27815 N. Harlow Pemberton Pkwy.<br>Ste 4200<br>Scottsdale, AZ 85391</div>
      <div class="office-divider"></div>
      <div class="office">6100 W. Cedar Avenue<br>Ste 700<br>Burbank, CA 91623</div>
    </address>

    <svg class="border-band" viewBox="0 0 540 140" preserveAspectRatio="none" aria-hidden="true">
      <defs>
        <linearGradient id="bandFill" x1="0" y1="0" x2="1" y2="1">
          <stop offset="0" stop-color="#2f2a8c"/>
          <stop offset="1" stop-color="#3f38a8"/>
        </linearGradient>
      </defs>
      <path d="M0 112 Q 330 104 540 4 L540 140 L0 140 Z" fill="url(#bandFill)"/>
      <path d="M30 100 Q 340 88 530 -4" fill="none" stroke="var(--brand-light)" stroke-width="2.5"/>
    </svg>
  </article>
</div>
</body>
</html>
```